Scented Candle Company Sticker Design for Packaging

We need a Sticker design for our various scented candle packages. Our handmade candles incorperate hand crafted Chiyogami Paper imported from Japan, which is wrapped around the jar. Each of the scents have different papers assigned to them and although we would like a general design in which the text can be changed according to each scent we would also like if the beautiful Japanese paper designs could be subtly incorporated in the design.

We want the the text of the sticker and logo of our company to be printed in gold foil once printed and our featured logo image is of a Dogwood tree. We think that perhaps the inclusion of dogwood blossom/s might look nice in the design but is not a must have!

We are fond of the delicate and classic print designs and etching designs. We would also like the design to be in a portrait rectangle that is closer in the shape of a square/ or not too long of a rectangle, and, would like to have a boarder on the edge of the sticker (this could incorporate the blossom if you wish, I have attached an image for reference/ inspiration) but we are after something much more simplistic and draws less attention to the eye and connected in the boarder.

Our brand is elegant and classic and we would like to be in keeping with our style. We have attached some images of the candles and our logo for inspiration, we do not want the stickers for the candle themselves but rather to place on the packaging.

Ive left some information for one of the candle scents for this design but once again I would like to reiterate that the design should allow for interchangeable titles for the other fragrances.

Japanese Cherry Blossom(in smaller writing).
Japanese cherry blossom, Orange blossom, cinnamon.

Our candles are hand made in Australia and a made from 100% soy wax and we would like to to be presented on the label.

I would like to mention again that we are looking for an elegant and classic design. We are looking for a simplistic design/layout that also focuses on the fine details. It should be striking but also not overbearing with an air of sophistication with minimal to no use of colours in encouraged.

I have also attached a font that is matched to the "candle co." underneath the tree in the logo.
Updates

I only just posted the design request, but first created the brief on the 2nd. I would like more time for the designers to both see my review and have an adequate amount of time to work on the project.

Target Market(s)

Up Market Shoppers.

Font styles to use
Script
Other font styles liked:
• Acorn

Colors
fbfbfb

Requirements
Must have
• Logo on the sticker.
Nice to have
• Nice to have a dogwood blossom incorporated into the boarder but must be simplistic as it doesn't want to be the main focus of the sticker
Should not have
• Photographs in the sticker design. Must be graphic design. No to little colour.

```html
<!DOCTYPE html>
<html lang="en">
<head>
<meta charset="utf-8">
<title>Larkspur Candle Co. – Sticker Labels</title>
<link rel="stylesheet" href="https://fonts.googleapis.com/css2?family=Didact+Gothic&display=swap">
<style>
  :root {
    --ink: #111111;
    --paper: #ffffff;
    --page: #ffffff;
    --blossom-ink: #d9d9d9;
    --gold: #d7a016;
    --gold-deep: #c48a0a;
    --gold-light: #f6d356;
    --gold-pale: #f7e7a6;
    --hairline: #b9b9b9;
  }
  * { box-sizing: border-box; margin: 0; padding: 0; }
  html, body {
    width: 1200px;
    height: 2859px;
    overflow: hidden;
    background: var(--page);
    font-family: "Didact Gothic", "Century Gothic", sans-serif;
  }
  .sheet { position: relative; width: 1200px; height: 2859px; }

  /* Sticker label component */
  .label {
    position: absolute;
    container-type: inline-size;
    background: var(--paper);
    border: 4px solid var(--ink);
    color: var(--ink);
    --frame: var(--ink);
    --accent: var(--ink);
    --blossom: var(--blossom-ink);
  }
  .label__frame {
    position: absolute;
    left: 7.5%; top: 7.6%; right: 10.5%; bottom: 9.8%;
    border: 0.75cqw solid var(--frame);
  }
  .label__blossoms {
    position: absolute; inset: 0;
    width: 100%; height: 100%;
  }
  .label__blossoms path { fill: var(--blossom); }
  .label__brand {
    position: absolute; left: 0; right: 0; top: 14.5%;
    display: flex; flex-direction: column; align-items: center;
    transform: translateX(1%);
  }
  .label__brand-dot {
    width: 5cqw; height: 5cqw; border-radius: 50%;
    background: var(--accent);
    margin-bottom: 1.6cqw;
  }
  .label__brand-name {
    font-size: 2.4cqw; letter-spacing: 0.3cqw;
    color: var(--accent); text-transform: uppercase; line-height: 1;
  }
  .label__title {
    position: absolute; left: 10%; right: 12%; top: 31%; height: 20%;
    display: flex; align-items: center; justify-content: center;
    text-align: center;
    font-size: 7.8cqw; font-weight: 400; line-height: 1.18;
    color: var(--accent);
  }
  .label--small .label__title {
    font-size: 6.6cqw; text-transform: uppercase; letter-spacing: 0.15cqw;
    top: 33%;
  }
  .label__icon {
    position: absolute; left: 51%; top: 61.8%;
    width: 5cqw; height: 5cqw; margin: -2.5cqw 0 0 -2.5cqw;
    border-radius: 50%;
    border: 0.35cqw solid var(--accent);
  }
  .label__facts {
    position: absolute; left: 0; right: 0; top: 74.4%;
    text-align: center; transform: translateX(1%);
    font-size: 2.1cqw; line-height: 2.55; color: var(--accent);
    font-family: Arial, "Didact Gothic", sans-serif;
  }
  .label--small .label__facts { font-weight: 700; font-size: 2.4cqw; }

  /* Sizes & placement */
  .label--feature { left: 141px; top: 124px; width: 902px; height: 989px; }
  .label--small { top: 1281px; width: 292px; height: 321px; border-width: 2px; }
  .label--cinnamon { left: 137px; }
  .label--peony { left: 457px; }
  .label--hawaiian { left: 776px; }
  .label--gold-fill, .label--gold-foil { top: 1656px; width: 432px; height: 474px; }
  .label--gold-fill {
    left: 134px; border: none;
    background: linear-gradient(90deg, var(--gold-deep) 0%, var(--gold) 35%, var(--gold-light) 75%, var(--gold-pale) 100%);
    --blossom: rgba(17,17,17,0.55);
  }
  .label--gold-foil {
    left: 635px; border: 2px solid var(--hairline);
    --frame: var(--gold); --accent: var(--gold);
    --blossom: rgba(215,160,22,0.45);
  }
  .label--gold-foil .label__frame, .label--gold-fill .label__frame { border-width: 0.6cqw; }
  .label--gold-foil .label__facts, .label--gold-fill .label__facts { font-weight: 700; }

  .mockup {
    position: absolute; left: 134px; top: 2202px; width: 921px; height: 519px;
    background:
      radial-gradient(ellipse 22% 40% at 50% 55%, #e9c9c4 0%, rgba(233,201,196,0) 100%),
      radial-gradient(ellipse 30% 30% at 48% 10%, #f3d08a 0%, rgba(243,208,138,0) 100%),
      linear-gradient(135deg, #2a1c12 0%, #4a3526 45%, #3a281b 70%, #1f150e 100%);
  }
</style>
</head>
<body>
<main class="sheet">

  <section class="label label--feature">
    <svg class="label__blossoms" viewBox="0 0 100 100" preserveAspectRatio="none" role="img" aria-label="Line-drawn four-petal flower clusters climbing the top-left and bottom-right corners of the frame">
      <path d="M1.5 4 H30 V14 H12 V41 H1.5 Z"/>
      <path d="M88 56 H95 V93 H65 V83 H88 Z"/>
    </svg>
    <div class="label__frame"></div>
    <div class="label__brand"><span class="label__brand-dot"></span><span class="label__brand-name">Larkspur Candle Co.</span></div>
    <h1 class="label__title">Japanese<br>Cherry Blossom</h1>
    <div class="label__icon" role="img" aria-label="Small outlined cherry blossom motif"></div>
    <p class="label__facts">HAND MADE IN AUSTRALIA<br>100% SOY WAX CANDLE</p>
  </section>

  <section class="label label--small label--cinnamon">
    <svg class="label__blossoms" viewBox="0 0 100 100" preserveAspectRatio="none" role="img" aria-label="Line-drawn flower corner clusters">
      <path d="M1.5 4 H30 V14 H12 V41 H1.5 Z"/><path d="M88 56 H95 V93 H65 V83 H88 Z"/>
    </svg>
    <div class="label__frame"></div>
    <div class="label__brand"><span class="label__brand-dot"></span><span class="label__brand-name">Larkspur Candle Co.</span></div>
    <h2 class="label__title">Cinnamon</h2>
    <div class="label__icon" role="img" aria-label="Small star anise motif"></div>
    <p class="label__facts">HAND MADE IN AUSTRALIA<br>100% SOY WAX CANDLE</p>
  </section>

  <section class="label label--small label--peony">
    <svg class="label__blossoms" viewBox="0 0 100 100" preserveAspectRatio="none" role="img" aria-label="Line-drawn flower corner clusters">
      <path d="M1.5 4 H30 V14 H12 V41 H1.5 Z"/><path d="M88 56 H95 V93 H65 V83 H88 Z"/>
    </svg>
    <div class="label__frame"></div>
    <div class="label__brand"><span class="label__brand-dot"></span><span class="label__brand-name">Larkspur Candle Co.</span></div>
    <h2 class="label__title">Peony Rose</h2>
    <div class="label__icon" role="img" aria-label="Small lotus-style petal motif"></div>
    <p class="label__facts">HAND MADE IN AUSTRALIA<br>100% SOY WAX CANDLE</p>
  </section>

  <section class="label label--small label--hawaiian">
    <svg class="label__blossoms" viewBox="0 0 100 100" preserveAspectRatio="none" role="img" aria-label="Line-drawn flower corner clusters">
      <path d="M1.5 4 H30 V14 H12 V41 H1.5 Z"/><path d="M88 56 H95 V93 H65 V83 H88 Z"/>
    </svg>
    <div class="label__frame"></div>
    <div class="label__brand"><span class="label__brand-dot"></span><span class="label__brand-name">Larkspur Candle Co.</span></div>
    <h2 class="label__title">Hawaian<br>Honey Blossom</h2>
    <div class="label__icon" role="img" aria-label="Small blossom motif"></div>
    <p class="label__facts">HAND MADE IN AUSTRALIA<br>100% SOY WAX CANDLE</p>
  </section>

  <section class="label label--gold-fill">
    <svg class="label__blossoms" viewBox="0 0 100 100" preserveAspectRatio="none" role="img" aria-label="Black line-drawn flower corner clusters on gold">
      <path d="M1.5 4 H30 V14 H12 V41 H1.5 Z"/><path d="M88 56 H95 V93 H65 V83 H88 Z"/>
    </svg>
    <div class="label__frame"></div>
    <div class="label__brand"><span class="label__brand-dot"></span><span class="label__brand-name">Larkspur Candle Co.</span></div>
    <h2 class="label__title">Japanese<br>Cherry Blossom</h2>
    <div class="label__icon" role="img" aria-label="Small cherry blossom motif"></div>
    <p class="label__facts">HAND MADE IN AUSTRALIA<br>100% SOY WAX CANDLE</p>
  </section>

  <section class="label label--gold-foil">
    <svg class="label__blossoms" viewBox="0 0 100 100" preserveAspectRatio="none" role="img" aria-label="Gold foil flower corner clusters">
      <path d="M1.5 4 H30 V14 H12 V41 H1.5 Z"/><path d="M88 56 H95 V93 H65 V83 H88 Z"/>
    </svg>
    <div class="label__frame"></div>
    <div class="label__brand"><span class="label__brand-dot"></span><span class="label__brand-name">Larkspur Candle Co.</span></div>
    <h2 class="label__title">Japanese<br>Cherry Blossom</h2>
    <div class="label__icon" role="img" aria-label="Small gold cherry blossom motif"></div>
    <p class="label__facts">HAND MADE IN AUSTRALIA<br>100% SOY WAX CANDLE</p>
  </section>

  <div class="mockup" role="img" aria-label="Photograph of a lit two-wick candle in a jar wrapped in pink cherry blossom paper with the gold label applied, on a dark wooden table"></div>

</main>
</body>
</html>
```